BRIM Outreach Partners Business Card Rebrand

Hello Designers! We are looking for help designing our new business card to go in conjunction with our company rebrand. Unfortunately, we have an event mid June that requires we get these printed ASAP (before our new website is launched.) We have a mostly complete Brand Book which I have uploaded to this request for your reference to company information, style, fonts. I've also enclosed our logo file in .eps & .jpg. Attached is a sample business card my boss liked but said was "too simple." I made it in Canva and do not profess to be a designer. NOT FOR DESIGN REFERENCE, ONLY FOR CONTEXT Here is what our old website looks like: https://brimoutreachpartners.com/.

```html
<!DOCTYPE html>
<html lang="en">
<head>
<meta charset="utf-8">
<title>BRIM Outreach Partners – Business Card</title>
<link href="https://fonts.googleapis.com/css2?family=Arimo:wght@400;700&display=swap" rel="stylesheet">
<style>
  :root {
    --brand-blue: #4db3e6;
    --ink: #111111;
    --card-white: #ffffff;
    --card-dark: #231f20;
    --backdrop: #e9eaec;
  }
  * { box-sizing: border-box; margin: 0; padding: 0; }
  html, body {
    width: 1200px;
    height: 1000px;
    overflow: hidden;
    background: var(--backdrop);
    font-family: "Arimo", Arial, sans-serif;
  }
  .canvas { position: relative; width: 1200px; height: 1000px; }
  .card {
    position: absolute;
    left: 303px;
    width: 593px;
    height: 338px;
  }
  .card--front { top: 108px; background: var(--card-white); color: var(--ink); }
  .card--back { top: 552px; background: var(--card-dark); }

  .brand {
    position: absolute;
    left: 0; right: 0;
    display: flex;
    align-items: center;
    justify-content: center;
    gap: 12px;
    font-weight: 700;
    white-space: nowrap;
  }
  .brand__dot { border-radius: 50%; background: var(--brand-blue); flex: none; }
  .card--front .brand { top: 40px; font-size: 26px; color: var(--ink); }
  .card--front .brand__dot { width: 70px; height: 70px; }
  .card--back .brand { top: 108px; font-size: 36px; color: #ffffff; gap: 16px; }
  .card--back .brand__dot { width: 120px; height: 120px; }

  .person {
    position: absolute;
    top: 168px; left: 0; right: 0;
    text-align: center;
  }
  .person__name { font-size: 30px; font-weight: 700; color: var(--brand-blue); line-height: 1.1; }
  .person__title { margin-top: 6px; font-size: 16px; letter-spacing: 0.5px; }
  .divider {
    position: absolute;
    top: 244px; left: 42px; right: 42px;
    height: 2px;
    background: var(--brand-blue);
  }
  .contact {
    position: absolute;
    top: 256px; left: 42px; right: 42px;
    font-size: 15px;
    line-height: 25px;
  }
  .contact__email { position: absolute; top: 0; right: 0; }
</style>
</head>
<body>
<main class="canvas">
  <section class="card card--front" aria-label="Business card front">
    <div class="brand"><span class="brand__dot"></span><span>BRIM Outreach Partners</span></div>
    <div class="person">
      <p class="person__name">Daniel Whitford-Lane</p>
      <p class="person__title">MANAGING PARTNER</p>
    </div>
    <div class="divider"></div>
    <div class="contact">
      <p class="contact__phone">+945-555-0143</p>
      <p class="contact__location">Nashville, TN Based (Central Time)</p>
      <p class="contact__email">daniel@brimoutreachpartners.com</p>
    </div>
  </section>

  <section class="card card--back" aria-label="Business card back">
    <div class="brand"><span class="brand__dot"></span><span>BRIM Outreach Partners</span></div>
  </section>
</main>
</body>
</html>
```